Business cards and stationery for small forestry/oilfield consulting company
Pine Ledger Consulting Ltd
Business cards and stationery for small forestry/oilfield consulting company - Environment
Creative Brief
Professional
K.J. Dorrin Waltby
RPFT
Box 42 Site 7 RR5 Alberta, Canada T0X 9Q7
pineledger@quorvanet.ca
The name of Pine Ledger Consulting Ltd is in the logo itself, not needed to repeat unless somehow artistically beneficial
Concepts
Business Cards, Letterhead, and Envelopes

```html
<!DOCTYPE html>
<html lang="en">
<head>
<meta charset="utf-8">
<title>Pine Ledger Consulting Ltd — Business Cards</title>
<link href="https://fonts.googleapis.com/css2?family=Cinzel:wght@400;600&display=swap" rel="stylesheet">
<style>
  :root {
    --bg: #e6e8e7;
    --green: #0f7a63;
    --green-deep: #0a5a49;
    --paper: #ffffff;
    --ink: #3a4a45;
    --swoosh: #9aa09e;
    --light: #eaf3f0;
  }
  * { margin: 0; padding: 0; box-sizing: border-box; }
  html, body { width: 1200px; height: 998px; overflow: hidden; background: var(--bg); }
  body { position: relative; font-family: "Cinzel", serif; }

  .card {
    position: absolute;
    width: 760px;
    height: 434px;
    border-radius: 26px;
    overflow: hidden;
    box-shadow: 0 14px 30px rgba(0,0,0,0.18);
  }
  .card--back {
    left: 390px; top: 50px;
    background: radial-gradient(ellipse at 45% 40%, var(--green) 0%, var(--green-deep) 100%);
    display: flex; align-items: center; justify-content: center;
  }
  .card--front { left: 50px; top: 514px; background: var(--paper); }
  .card-art { position: absolute; inset: 0; }

  .brand { text-align: center; line-height: 1; }
  .brand-name { font-weight: 600; font-size: 46px; letter-spacing: 1px; }
  .brand-sub { font-weight: 600; font-size: 20px; letter-spacing: 7px; margin-top: 8px; }
  .card--back .brand { color: var(--light); }
  .card--front .brand {
    position: absolute; left: 28px; top: 130px; width: 310px; color: var(--ink);
  }
  .card--front .brand-name { font-size: 38px; }
  .card--front .brand-sub { font-size: 17px; letter-spacing: 6px; }

  .holder {
    position: absolute; left: 420px; top: 128px; color: var(--light);
  }
  .holder-name { font-size: 20px; letter-spacing: 1px; }
  .holder-title { font-size: 13px; letter-spacing: 2px; margin-top: 4px; }

  .contact {
    position: absolute; left: 405px; top: 208px; list-style: none; color: var(--light);
    font-size: 13px; letter-spacing: 0.5px;
  }
  .contact li { display: flex; align-items: flex-start; gap: 12px; margin-bottom: 10px; }
  .contact .icon { width: 18px; height: 18px; flex: none; }
  .contact span { line-height: 18px; }
</style>
</head>
<body>

  <section class="card card--back" aria-label="Business card back">
    <div class="brand">
      <div class="brand-name">PINE LEDGER</div>
      <div class="brand-sub">CONSULTING LTD</div>
    </div>
  </section>

  <section class="card card--front" aria-label="Business card front">
    <svg class="card-art" viewBox="0 0 760 434" aria-hidden="true">
      <defs>
        <radialGradient id="panelGreen" cx="70%" cy="45%" r="70%">
          <stop offset="0" stop-color="#0f7a63"/>
          <stop offset="1" stop-color="#0a5a49"/>
        </radialGradient>
      </defs>
      <path d="M372,0 C322,140 318,290 356,434 L366,434 C334,290 340,140 392,0 Z" fill="var(--swoosh)"/>
      <path d="M402,0 C346,140 344,290 378,434 L760,434 L760,0 Z" fill="url(#panelGreen)"/>
    </svg>

    <div class="brand">
      <div class="brand-name">PINE LEDGER</div>
      <div class="brand-sub">CONSULTING LTD</div>
    </div>

    <div class="holder">
      <div class="holder-name">K.J. DORRIN WALTBY</div>
      <div class="holder-title">RPFT</div>
    </div>

    <ul class="contact">
      <li>
        <svg class="icon" viewBox="0 0 18 18"><circle cx="9" cy="9" r="9" fill="#eaf3f0"/><path d="M9 4a3 3 0 0 0-3 3c0 2.3 3 6 3 6s3-3.7 3-6a3 3 0 0 0-3-3z" fill="#0a5a49"/></svg>
        <span>Box 42 Site 7 RR5<br>Alberta, Canada T0X 9Q7</span>
      </li>
      <li>
        <svg class="icon" viewBox="0 0 18 18"><circle cx="9" cy="9" r="9" fill="#eaf3f0"/><path d="M6 4.5l2 2-1 1.3a6 6 0 0 0 2.7 2.7l1.3-1 2 2-1.3 1.5C8.5 13 5 9.5 4.5 5.8z" fill="#0a5a49"/></svg>
        <span>403-555-0142</span>
      </li>
      <li>
        <svg class="icon" viewBox="0 0 18 18"><circle cx="9" cy="9" r="9" fill="#eaf3f0"/><rect x="4.5" y="6" width="9" height="6.5" fill="none" stroke="#0a5a49" stroke-width="1.3"/><path d="M4.5 6l4.5 3.5L13.5 6" fill="none" stroke="#0a5a49" stroke-width="1.3"/></svg>
        <span>pineledger@quorvanet.ca</span>
      </li>
      <li>
        <svg class="icon" viewBox="0 0 18 18"><circle cx="9" cy="9" r="9" fill="#eaf3f0"/><circle cx="9" cy="9" r="4.5" fill="none" stroke="#0a5a49" stroke-width="1.2"/><path d="M4.5 9h9M9 4.5c-2 2.5-2 6.5 0 9M9 4.5c2 2.5 2 6.5 0 9" fill="none" stroke="#0a5a49" stroke-width="1"/></svg>
        <span>www.quorvanet.ca</span>
      </li>
    </ul>
  </section>

</body>
</html>
```